Letterhead design for Dental Practice - Ashby Lane Dental Care

Letterhead for Private Dental Practice. To be used for all official correspondance and for printing treatment details on to be given to patients.

Target Market(s)

Private dental patients

Industry/Entity Type

Dental Clinic

Font styles to use
Other font styles liked:
• nexa-light

Colors
33a6d7
1c66ac
85abd2

Requirements
Must have
• info in the footer and header needs to be 3.5cm from upper/lower boader of paper, see photo in uploaded files
• info details:
• tel. 0115 947 3051
• email info@ashbylanedc.co.uk
• ashbylanedentalcare.co.uk
• 17b Ashby Lane West Bridgford Nottingham NG2 7QT
• nexa-light font as in uploaded logo files
Should not have
• No funny tooth pictures

```html
<!DOCTYPE html>
<html lang="en">
<head>
<meta charset="utf-8">
<title>Ashby Lane Dental Care – Letterhead</title>
<link href="https://fonts.googleapis.com/css2?family=Questrial&family=Open+Sans:wght@400&family=Arimo:wght@700&display=swap" rel="stylesheet">
<style>
  :root {
    --bg: #e4e5e6;
    --paper: #ffffff;
    --sky: #33a6d7;
    --navy: #1c66ac;
    --mist: #85abd2;
    --ink: #2a2a2a;
    --muted: #555a5e;
    --rule: #b9d49a;
  }
  * { box-sizing: border-box; margin: 0; padding: 0; }
  html, body { width: 1200px; height: 945px; overflow: hidden; background: var(--bg); }
  .letterhead {
    position: absolute; left: 280px; top: 18px;
    width: 640px; height: 905px;
    background: var(--paper);
    box-shadow: 0 4px 18px rgba(0,0,0,0.12);
    overflow: hidden;
  }
  .header-band {
    position: absolute; left: 0; top: 0; width: 640px; height: 96px;
    background: linear-gradient(90deg, var(--navy), var(--sky) 50%, var(--navy));
  }
  .brand {
    position: absolute; left: 56px; top: 128px;
    display: flex; align-items: center; gap: 10px;
    font-family: "Questrial", sans-serif; font-size: 22px; line-height: 1.2; color: var(--sky);
    letter-spacing: 0.5px; white-space: nowrap;
  }
  .brand-dot { width: 14px; height: 14px; border-radius: 50%; background: var(--sky); flex: none; }
  .letter-body {
    position: absolute; left: 80px; top: 232px; width: 470px;
    font-family: "Open Sans", sans-serif; font-size: 11.5px; line-height: 1.45; color: var(--ink);
  }
  .greeting { font-family: "Arimo", sans-serif; font-weight: 700; font-size: 13px; margin-bottom: 14px; }
  .letter-body p { margin-bottom: 16px; }
  .signature {
    width: 150px; height: 56px; margin-top: 18px;
    background: linear-gradient(90deg, #f1f1f1, #e6e6e6);
    border-radius: 4px;
  }
  .footer {
    position: absolute; left: 80px; right: 48px; top: 800px;
    border-top: 1px solid var(--rule);
    padding-top: 10px; text-align: right;
    font-family: "Questrial", sans-serif; font-size: 10.5px; color: var(--muted); line-height: 1.6;
    white-space: nowrap;
  }
  .footer b { color: var(--ink); font-weight: 400; }
  .footer span { color: var(--muted); }
</style>
</head>
<body>
  <main class="letterhead">
    <div class="header-band" role="img" aria-label="Decorative blue header wave"></div>

    <div class="brand"><span class="brand-dot"></span>Ashby Lane Dental Care</div>

    <section class="letter-body">
      <p class="greeting">Dear Mr. Harlow,</p>
      <p>Lorem Ipsum is simply dummy text of the printing and typesetting industry. Lorem Ipsum has been the industry's standard dummy text ever since the 1500s, when an unknown printer took a galley of type and scrambled it to make a type specimen book. It has survived not only five centuries, but also the leap into electronic typesetting, remaining essentially unchanged.</p>
      <p>The standard chunk of Lorem Ipsum used since the 1500s is reproduced below for those interested. Sections 1.10.32 and 1.10.33 from "de Finibus Bonorum et Malorum" by Verano are also reproduced in their exact original form, accompanied by English versions from the 1914 translation by H. Castell.</p>
      <p>Lorem Ipsum is simply dummy text of the printing and typesetting industry. Lorem Ipsum has been the industry's standard dummy text ever since the 1500s, when an unknown printer took a galley of type and scrambled it to make a type specimen book. It has survived not only five centuries, but also the leap into electronic typesetting, remaining essentially unchanged. It was popularised in the</p>
      <div class="signature" role="img" aria-label="Handwritten signature of the sender"></div>
    </section>

    <footer class="footer">
      <div><b>P:</b> <span>0115 947 3051</span> &nbsp;<b>E:</b> <span>info@ashbylanedc.co.uk</span> &nbsp;|&nbsp; <span>www.ashbylanedentalcare.co.uk</span></div>
      <div>17b Ashby Lane, West Bridgford, Nottingham NG2 7QT</div>
    </footer>
  </main>
</body>
</html>
```